Professional services business card

This is for a new business in New Zealand, providing professional advice to boards of directors of companies
The point of difference is a strong blend of Financial and IT knowledge

Target audience are senior business executives, CEO/CFO/President, etc.
So, simple but appealing
Business colours are orange and blue

Sample logo attached
proposed Content also attached - feedback on wording is welcome
Updates

Please provide for a logo to be added - about 30 mm wide and 10 mm high

the company name is "Korvale Meridian Ltd" - logo now uploaded to the project brief

Information to include are now in the second file that was uploaded

Industry/Entity Type

Business

```html
<!DOCTYPE html>
<html lang="en">
<head>
<meta charset="utf-8">
<title>Korvale Meridian – Business Card</title>
<link rel="stylesheet" href="https://fonts.googleapis.com/css2?family=Questrial&display=swap">
<style>
  :root {
    --backdrop: #2b2b2b;
    --orange: #f0901e;
    --orange-dark: #e07f10;
    --blue: #1a8cc8;
    --white: #ffffff;
    --card-white: #ffffff;
    --text-font: "Questrial", "Century Gothic", sans-serif;
  }
  * { box-sizing: border-box; margin: 0; padding: 0; }
  html, body { width: 1200px; height: 900px; overflow: hidden; }
  body {
    background: var(--backdrop);
    font-family: var(--text-font);
    position: relative;
  }
  .card {
    position: absolute;
    top: 302px;
    width: 514px;
    height: 296px;
    overflow: hidden;
  }
  .card--front { left: 71px; background: var(--orange); color: var(--white); }
  .card--back { left: 615px; background: var(--card-white); color: var(--blue); }

  .brand {
    display: flex;
    align-items: center;
    gap: 8px;
    font-size: 25px;
    line-height: 1.05;
    color: var(--blue);
    letter-spacing: 0.2px;
  }
  .brand__dot {
    width: 14px; height: 14px; border-radius: 50%;
    background: var(--orange); flex: none;
  }
  .card--front .brand__dot { background: var(--white); }

  .card--front .brand { position: absolute; left: 50px; top: 132px; }

  .services {
    position: absolute;
    left: 281px;
    top: 98px;
    padding-left: 10px;
    border-left: 1.5px solid var(--white);
  }
  .services__title { font-size: 12px; font-weight: 700; letter-spacing: 0.2px; margin-bottom: 3px; }
  .services__list { list-style: none; }
  .services__item { font-size: 13px; line-height: 18px; display: flex; align-items: center; gap: 6px; }
  .services__item svg { width: 10px; height: 10px; flex: none; }

  .website {
    position: absolute;
    left: 206px; top: 262px;
    font-size: 12px; font-weight: 700;
  }

  .card--back .brand { position: absolute; left: 50px; top: 52px; }
  .person { position: absolute; left: 80px; top: 146px; }
  .person__name { font-size: 15px; font-weight: 700; }
  .person__creds { font-size: 11px; font-weight: 400; }
  .person__role { font-size: 12px; margin-top: 1px; }

  .contact { position: absolute; left: 80px; top: 197px; font-size: 12px; line-height: 17.5px; }
  .contact__company { font-weight: 700; }
  .contact__row { display: flex; align-items: center; gap: 5px; }
  .contact__row svg { width: 11px; height: 11px; flex: none; }

  .address-band {
    position: absolute; left: 0; right: 0; bottom: 0;
    height: 28px; background: var(--orange);
    color: var(--white); font-size: 12px;
    padding-left: 80px; line-height: 28px;
  }
</style>
</head>
<body>

<section class="card card--front" aria-label="Card front">
  <div class="brand"><span class="brand__dot"></span><span>Korvale Meridian</span></div>

  <div class="services">
    <p class="services__title">TALK TO US AFTER ABOUT</p>
    <ul class="services__list">
      <li class="services__item"><svg viewBox="0 0 10 10"><path d="M1 9 L9 1 M3 1 H9 V7" fill="none" stroke="#fff" stroke-width="1.3"/></svg>Governance</li>
      <li class="services__item"><svg viewBox="0 0 10 10"><path d="M1 9 L9 1 M3 1 H9 V7" fill="none" stroke="#fff" stroke-width="1.3"/></svg>Good Stewardship</li>
      <li class="services__item"><svg viewBox="0 0 10 10"><path d="M1 9 L9 1 M3 1 H9 V7" fill="none" stroke="#fff" stroke-width="1.3"/></svg>Financial Management Insight</li>
      <li class="services__item"><svg viewBox="0 0 10 10"><path d="M1 9 L9 1 M3 1 H9 V7" fill="none" stroke="#fff" stroke-width="1.3"/></svg>Information Technology Insight</li>
      <li class="services__item"><svg viewBox="0 0 10 10"><path d="M1 9 L9 1 M3 1 H9 V7" fill="none" stroke="#fff" stroke-width="1.3"/></svg>Mentoring and Business Advice</li>
    </ul>
  </div>

  <p class="website">www.korvale.co.nz</p>
</section>

<section class="card card--back" aria-label="Card back">
  <div class="brand"><span class="brand__dot"></span><span>Korvale Meridian</span></div>

  <div class="person">
    <p class="person__name">Tamsin Ahearn<span class="person__creds">, M.Com, ACA(NZ), ACMA</span></p>
    <p class="person__role">Director</p>
  </div>

  <div class="contact">
    <p class="contact__company">Korvale Meridian Ltd</p>
    <p class="contact__row"><svg viewBox="0 0 12 12"><path d="M3 1 L5 3.5 L4 5 C4.6 6.4 5.6 7.4 7 8 L8.5 7 L11 9 L9.5 11 C5 10.5 1.5 7 1 2.5 Z" fill="none" stroke="#1a8cc8" stroke-width="1"/></svg>021 555 0147</p>
    <p class="contact__row"><svg viewBox="0 0 12 12"><rect x="1" y="3" width="10" height="7" fill="#1a8cc8"/><path d="M1 3 L6 7 L11 3" fill="none" stroke="#fff" stroke-width="0.9"/></svg>Tamsin.Ahearn@korvale.co.nz</p>
    <p class="contact__row"><svg viewBox="0 0 12 12"><rect x="1" y="1" width="10" height="10" rx="1" fill="#1a8cc8"/></svg>www.profilehub.co.nz/tamsinahearn</p>
  </div>

  <p class="address-band">PO Box 20417, Lambton Quay, Wellington, 6145</p>
</section>

</body>
</html>
```